Zorvo Salsa label for 16oz jar

We need a design for a label for a 16oz glass jar for salsa (dimensions in inches- 2.75 x9.5). Name of salsa is “Zorvo Salsa” and needs to include a place for medium or hot for the different flavors. Looking for bright Fiesta colors but a mature look. Attached is an image of the coloring scheme we like. There will need to be nutrition facts on one end and a description of the product/flavor on the other side of the label. Ultimately at this point looking for brand design.

```html
<!DOCTYPE html>
<html lang="en">
<head>
<meta charset="utf-8">
<title>Zorvo Salsa – Jar Label</title>
<link rel="stylesheet" href="https://fonts.googleapis.com/css2?family=Almendra+SC&family=Archivo+Black&family=Libre+Franklin:wght@400;600;700;800&display=swap">
<style>
  :root {
    --page: #f1f1f1;
    --white: #ffffff;
    --navy: #1b4fa0;
    --royal: #1d5bb8;
    --sky: #cfe6f7;
    --sky-deep: #3ea3e0;
    --sun: #ffc21a;
    --chili: #e8232f;
    --rose: #f26a7a;
    --tangerine: #f47a2b;
    --lime: #97c93d;
    --ink: #1a1a1a;
    --energy: #e1202c;
    --fat: #f7a81b;
    --satfat: #f7a81b;
    --sugar: #22b39a;
    --salt: #22b39a;
  }
  * { box-sizing: border-box; margin: 0; padding: 0; }
  html, body { width: 1200px; height: 860px; overflow: hidden; background: var(--page); }
  .label {
    position: absolute; left: 30px; top: 256px; width: 1140px; height: 348px;
    background: var(--white); overflow: hidden;
    box-shadow: 0 4px 10px rgba(0,0,0,.25);
  }
  .label__bands { position: absolute; inset: 0; }
  .label__ground {
    position: absolute; left: 0; right: 0; bottom: 0; height: 89px; background: var(--lime);
  }
  .story {
    position: absolute; left: 14px; top: 13px; width: 353px; height: 228px;
    background: rgba(214, 234, 248, .85);
  }
  .story__text {
    font-family: "Almendra SC", serif; color: var(--ink); font-size: 11.4px; line-height: 14.6px;
    text-align: center; padding: 14px 22px 0;
  }
  .badges { position: absolute; left: 51px; top: 165px; display: flex; gap: 13px; }
  .badge {
    width: 46px; height: 62px; border: 1.6px solid var(--ink); border-radius: 9px 9px 22px 22px;
    background: var(--white); font-family: "Libre Franklin", sans-serif; text-align: center;
    padding-top: 5px; overflow: hidden; position: relative;
  }
  .badge__name { font-size: 10.5px; line-height: 11px; height: 22px; display:flex; align-items:center; justify-content:center; }
  .badge__name--tight { font-size: 8.5px; line-height: 9px; }
  .badge__value { font-size: 10.5px; font-weight: 700; line-height: 12px; }
  .badge__pct {
    position: absolute; left: 4px; right: 4px; bottom: 4px; height: 17px; border-radius: 3px 3px 14px 14px;
    color: var(--white); font-size: 11px; font-weight: 600; line-height: 17px;
  }
  .story-footer {
    position: absolute; left: 40px; width: 290px; top: 276px; text-align: center;
    font-family: "Almendra SC", serif; color: var(--navy); font-size: 11.4px; line-height: 14.6px;
  }
  .brand {
    position: absolute; left: 384px; top: 40px; width: 370px; text-align: center;
    font-family: "Almendra SC", serif; color: var(--navy); font-size: 74px; line-height: 76px;
    letter-spacing: 1px;
  }
  .variant {
    position: absolute; left: 437px; top: 235px; width: 267px; height: 53px; border-radius: 27px;
    background: var(--chili); color: var(--white); text-align: center;
    font-family: "Almendra SC", serif; font-size: 36px; line-height: 53px;
  }
  .tagline {
    position: absolute; left: 450px; width: 240px; top: 303px; text-align: center;
    font-family: "Almendra SC", serif; color: var(--navy); font-size: 12.5px; line-height: 16px;
  }
  .facts {
    position: absolute; left: 812px; top: 40px; width: 293px; height: 270px;
    background: var(--white); border: 1.5px solid var(--ink); padding: 4px 6px;
    font-family: "Libre Franklin", sans-serif; color: var(--ink); font-size: 7.3px; line-height: 12px;
  }
  .facts__title { font-family: "Archivo Black", sans-serif; font-size: 28px; line-height: 32px; border-bottom: 1px solid var(--ink); }
  .facts__row { display: flex; justify-content: space-between; border-bottom: .6px solid #555; }
  .facts__row--thick { border-bottom: 5px solid var(--ink); }
  .facts__row--mid { border-bottom: 2.5px solid var(--ink); }
  .facts__serving { font-weight: 800; font-size: 9.5px; }
  .facts__small { font-size: 5.5px; font-weight: 700; line-height: 8px; }
  .facts__cal { font-weight: 800; font-size: 17px; line-height: 18px; }
  .facts__dv { justify-content: flex-end; font-weight: 700; font-size: 6px; }
  .indent1 { padding-left: 12px; }
  .indent2 { padding-left: 24px; }
  .b { font-weight: 700; }
  .facts__note { font-size: 6px; line-height: 7.5px; padding-top: 4px; border-top: 4px solid var(--ink); margin-top: 2px; }
</style>
</head>
<body>
  <section class="label" aria-label="Zorvo Salsa jar label">
    <svg class="label__bands" width="1140" height="348" viewBox="0 0 1140 348" aria-hidden="true">
      <defs>
        <linearGradient id="skyBand" x1="0" y1="0" x2="1" y2="0">
          <stop offset="0" stop-color="#2f8fd6"/><stop offset="1" stop-color="#8fcdf2"/>
        </linearGradient>
        <linearGradient id="roseBand" x1="0" y1="0" x2="1" y2="0">
          <stop offset="0" stop-color="#f7b6be"/><stop offset="1" stop-color="#e8232f"/>
        </linearGradient>
      </defs>
      <path d="M0 0 H640 L420 150 L0 120 Z" fill="url(#skyBand)"/>
      <path d="M0 0 H470 L320 80 L0 60 Z" fill="#1d6fc4"/>
      <path d="M370 175 L640 55 L760 0 H830 L580 120 Z" fill="var(--sun)"/>
      <path d="M660 70 Q860 5 1140 40 V0 H720 Z" fill="url(#roseBand)"/>
      <path d="M760 40 Q940 0 1140 85 V40 Q960 -10 760 40 Z" fill="var(--chili)"/>
      <path d="M1010 0 H1140 V110 Q1100 40 1010 0 Z" fill="var(--tangerine)"/>
    </svg>
    <div class="label__ground"></div>

    <div class="story">
      <p class="story__text">Lorem ipsum dolor sit amet, consectetuer adipiscing elit, sed diam nonummy nibh euismod tincidunt ut laoreet dolore magna aliquam erat volutpat. Ut wisi enim ad minim veniam, quis nostrud exerci tation ullamcorper suscipit lobortis nisl ut aliquip ex ea commodo consequat. Duis autem vel eum iriure dolor in</p>
    </div>

    <div class="badges">
      <div class="badge"><div class="badge__name">Energy</div><div class="badge__value">245kcal</div><div class="badge__pct" style="background:var(--energy)">12%</div></div>
      <div class="badge"><div class="badge__name">Fat</div><div class="badge__value">12g</div><div class="badge__pct" style="background:var(--fat)">14%</div></div>
      <div class="badge"><div class="badge__name badge__name--tight">Satura-<br>ted Fat</div><div class="badge__value">2g</div><div class="badge__pct" style="background:var(--satfat)">10%</div></div>
      <div class="badge"><div class="badge__name">Sugars</div><div class="badge__value">4g</div><div class="badge__pct" style="background:var(--sugar)">8%</div></div>
      <div class="badge"><div class="badge__name">Salt</div><div class="badge__value">0.2g</div><div class="badge__pct" style="background:var(--salt)">9%</div></div>
    </div>

    <p class="story-footer">Lorem ipsum dolor sit amet, consectetuer adipiscing elit, sed diam nonummy nibh euismod tincidunt ut laoreet dolore magna</p>

    <h1 class="brand">Zorvo<br>Salsa</h1>
    <div class="variant">Red Sauce</div>
    <p class="tagline">For natural and genuie products branding</p>

    <div class="facts">
      <div class="facts__title">Nutrition Facts</div>
      <div style="font-size:8px">4 servings per container/6 raciones por envase</div>
      <div class="facts__row facts__row--thick facts__serving"><span>Serving size</span><span>1 cup/1 taza (180g)</span></div>
      <div class="facts__small">Amount per serving</div>
      <div class="facts__row facts__row--mid facts__cal"><span>Calories</span><span>245</span></div>
      <div class="facts__row facts__dv"><span>% Daily Value*/% Valor diario*</span></div>
      <div class="facts__row"><span><span class="b">Total Fat/Grasa total</span> 12g</span><span class="b">14%</span></div>
      <div class="facts__row indent1"><span>Saturated Fat/Grasa Saturada 2g</span><span class="b">10%</span></div>
      <div class="facts__row indent1"><span><i>Trans</i> Fat/Grasa <i>Trans</i> 0g</span><span></span></div>
      <div class="facts__row"><span><span class="b">Cholesterol/Colesterol</span> 8mg</span><span class="b">3%</span></div>
      <div class="facts__row"><span><span class="b">Sodium/Sodio</span> 210mg</span><span class="b">9%</span></div>
      <div class="facts__row"><span><span class="b">Total Carbohydrate/Carbohidrato Total</span> 34g</span><span class="b">12%</span></div>
      <div class="facts__row indent1"><span>Dietary Fiber/Fibra Dietética 7g</span><span class="b">25%</span></div>
      <div class="facts__row indent1"><span>Total Sugars/Azúcares Totales 5g</span><span></span></div>
      <div class="facts__row indent2"><span>Includes 4g Added Sugars/Incluye 4 g de azúcares añadidos</span><span class="b">8%</span></div>
      <div class="facts__row" style="border:0"><span><span class="b">Protein/Proteínas</span> 11g</span><span></span></div>
      <div class="facts__note">* The % Daily Value (DV) tells you how much a nutrient in a serving of food contributes to a daily diet. 2,000 calories a day is used for general nutrition advice.</div>
    </div>
  </section>
</body>
</html>
```